QRV designs

qrv designs is an interior design firm in omaha, NE. Offering complete residential/commercial design. Exterior, int finishes, cabinets, furniture, window covering. Have been in business for 25 yrs. Lived in and/or completed work in LA, NYC, PHX, MIami, London, Canada, Mexico. We would like to see a marketing flyer with clean, architectural design. Modern .Flyer will be on display at open houses & mailed to perspective clients. Dont want a lot of color. Prefer whites/black, greys or brown. Maybe small accent of blue like logo. Block architectural lettering. do not need to use all photos. but use at least one from each of the three projects. thanks for you time
Updates

please change/add on any and all submissions the following add: Dana Whitcombe, Principal (in info section not on logo) change: Info@qrvdesigns.com, not dana @qrvdesigns.com add: back design, would like to use as many photos as possible thanks you

Industry/Entity Type

Residential

```html
<!DOCTYPE html>
<html lang="en">
<head>
<meta charset="utf-8">
<title>QRV designs – We can work with your Builder</title>
<link href="https://fonts.googleapis.com/css2?family=Noto+Serif:wght@400;700&family=Arimo:wght@400;700&display=swap" rel="stylesheet">
<style>
  :root {
    --brown-dark: #2e1f17;
    --brown-mid: #3d2a20;
    --brown-line: #4a3529;
    --accent-blue: #1f66b0;
    --ink: #1b1b1b;
    --paper: #ffffff;
    --stage: #e6e5e2;
  }
  * { box-sizing: border-box; margin: 0; padding: 0; }
  html, body { width: 1200px; height: 1000px; overflow: hidden; }
  body { background: var(--stage); position: relative; font-family: "Noto Serif", Georgia, serif; }

  .flyer {
    position: absolute; left: 299px; top: 36px; width: 604px; height: 930px;
    background: var(--paper); box-shadow: 0 4px 18px rgba(0,0,0,.25);
  }

  .masthead {
    position: absolute; left: 0; top: 0; width: 604px; height: 160px;
    background: var(--brown-dark);
  }
  .brand-panel {
    position: absolute; left: 16px; top: 0; width: 202px; height: 160px;
    background: var(--brown-mid);
    border-left: 6px solid var(--brown-line); border-right: 6px solid var(--brown-line);
  }
  .brand-name {
    position: absolute; left: 0; width: 190px; top: 62px; text-align: center;
    color: var(--paper); font-size: 26px; font-weight: 400; line-height: 36px;
    white-space: nowrap;
  }
  .headline {
    position: absolute; left: 250px; top: 32px; color: var(--paper);
    font-size: 38px; line-height: 52px; font-weight: 400; white-space: nowrap;
  }
  .headline b { font-weight: 700; }
  .masthead-rule {
    position: absolute; left: 0; top: 163px; width: 604px; height: 2px; background: var(--brown-dark);
  }

  .intro {
    position: absolute; left: 17px; top: 207px; width: 566px;
    font-size: 15.5px; line-height: 29px; color: var(--ink); text-align: justify;
  }
  .intro b { font-weight: 700; }

  .gallery-title {
    position: absolute; left: 89px; top: 330px; width: 444px; height: 52px;
  }
  .gallery-title svg { position: absolute; left: 0; top: 0; }
  .gallery-title h2 {
    position: absolute; left: 0; width: 100%; top: 8px; text-align: center;
    color: var(--paper); font-size: 25px; font-weight: 700;
  }

  .project-photo {
    position: absolute; border: 4px solid var(--paper);
    box-shadow: 0 1px 5px rgba(0,0,0,.45);
  }
  .photo-great-room { left: 18px; top: 424px; width: 175px; height: 120px; background: linear-gradient(160deg,#3a3431,#1d1a19 60%,#6d6660); }
  .photo-bath { left: 216px; top: 424px; width: 175px; height: 120px; background: linear-gradient(180deg,#2a2626,#4a4646 55%,#bdbab6); }
  .photo-wine { left: 18px; top: 560px; width: 175px; height: 118px; background: linear-gradient(120deg,#4b2e22,#7a5843 55%,#d8c2a2); }
  .photo-bar { left: 216px; top: 560px; width: 175px; height: 118px; background: linear-gradient(180deg,#5b4c40,#3a2b22 55%,#6e5a48); }
  .photo-kitchen { left: 410px; top: 424px; width: 173px; height: 258px; background: linear-gradient(180deg,#d9c7a4,#efe3c8 45%,#cbb792 80%,#4a3a2c); }

  .call-line {
    position: absolute; left: 40px; top: 736px; color: var(--accent-blue);
    font-size: 44px; font-weight: 700; line-height: 56px; white-space: nowrap;
  }
  .call-number {
    position: absolute; left: 302px; top: 736px; color: #000;
    font-family: "Arimo", Arial, sans-serif; font-weight: 700; font-size: 38px; white-space: nowrap;
  }
  .call-sub {
    position: absolute; left: 40px; top: 788px; color: var(--accent-blue);
    font-size: 27px; font-weight: 700; white-space: nowrap;
  }

  .contact-bar {
    position: absolute; left: 0; top: 868px; width: 604px; height: 62px;
    background: var(--brown-dark); color: var(--paper);
    font-family: "Arimo", Arial, sans-serif; font-size: 18px;
    display: flex; align-items: center; justify-content: center; gap: 8px;
    white-space: nowrap;
  }
  .contact-item { display: inline-flex; align-items: center; gap: 5px; }
  .contact-item svg { flex: none; }
</style>
</head>
<body>
<main class="flyer">
  <header class="masthead">
    <div class="brand-panel">
      <div class="brand-name">QRV designs</div>
    </div>
    <h1 class="headline"><b>We</b> can work<br>with your <b>Builder</b></h1>
  </header>
  <div class="masthead-rule"></div>

  <p class="intro"><b>We</b> can work with your <b>Builder</b> to coordinate the many <b>Architectural</b> details required to create your <b>Personal Space.</b>&nbsp; Thus allowing your proj&shy;ect to progress <b>Smoothly</b> and more cost <b>Effectively.</b></p>

  <div class="gallery-title">
    <svg width="444" height="52" viewBox="0 0 444 52">
      <rect x="0" y="13" width="444" height="26" fill="#2e1f17"/>
      <rect x="14" y="0" width="408" height="52" fill="#2e1f17"/>
      <rect x="16" y="13" width="26" height="26" fill="#fff"/>
      <rect x="394" y="13" width="26" height="26" fill="#fff"/>
    </svg>
    <h2>Our Project Gallery</h2>
  </div>

  <div class="project-photo photo-great-room" role="img" aria-label="Photo of a vaulted great room with dark beams and a kitchen island"></div>
  <div class="project-photo photo-bath" role="img" aria-label="Photo of a dark modern bathroom with a freestanding tub"></div>
  <div class="project-photo photo-kitchen" role="img" aria-label="Photo of a cream kitchen with ornate cabinets and a range hood"></div>
  <div class="project-photo photo-wine" role="img" aria-label="Photo of a stone wine niche with arched display"></div>
  <div class="project-photo photo-bar" role="img" aria-label="Photo of a basement bar with granite counter and stools"></div>

  <div class="call-line">Please Call</div>
  <div class="call-number">402-555-0148</div>
  <div class="call-sub">to Talk About Your Upcoming Project</div>

  <footer class="contact-bar">
    <span class="contact-item">
      <svg width="15" height="11" viewBox="0 0 15 11"><rect x="0.5" y="0.5" width="14" height="10" fill="#fff"/><path d="M1 1 L7.5 6 L14 1" stroke="#2e1f17" stroke-width="1.3" fill="none"/></svg>
      info@qrvdesigns.com
    </span>
    <span class="contact-item">
      <svg width="15" height="15" viewBox="0 0 16 16" fill="none" stroke="#fff" stroke-width="1.2"><circle cx="8" cy="8" r="7"/><ellipse cx="8" cy="8" rx="3" ry="7"/><path d="M1 8h14M2.5 4.5h11M2.5 11.5h11"/></svg>
      www.qrvdesigns.com
    </span>
    <span class="contact-item">
      <svg width="14" height="16" viewBox="0 0 14 16"><rect x="0" y="0" width="14" height="16" rx="2" fill="#fff"/><path d="M4 3c-1 1-1 3 1 6s4 4 5 3l.8-1-2-1.5-.9.8c-.8-.3-2.2-2-2.4-2.8l.8-.9L5.2 2.5z" fill="#2e1f17"/></svg>
      402-555-0148
    </span>
  </footer>
</main>
</body>
</html>
```